Webdesign für Hausmeisterservice, Garten- und Landschaftsbau
Zielgruppe
Hausmeisterservice und Garten und Landschaftsbau
Aufgabenstellung
habe schon eine Webseite erstellt die muss Designt werden. Wohnpfleger.info

```html
<!DOCTYPE html>
<html lang="de">
<head>
<meta charset="utf-8">
<title>Wohnpfleger – Garten &amp; Landschaftsbau</title>
<link rel="stylesheet" href="https://fonts.googleapis.com/css2?family=Open+Sans:wght@400;600;700&display=swap">
<style>
:root{
  --red:#ab3a3c;
  --footer:#b03c3e;
  --blue:#1b5fa2;
  --ink:#1c1c1c;
  --text:#2b2b2b;
  --hero-bg:#ebebeb;
  --hero-shade:#e1e1e1;
  --white:#ffffff;
}
*{margin:0;padding:0;box-sizing:border-box}
html,body{width:1200px;height:3055px;overflow:hidden;background:var(--white)}
body{position:relative;font-family:"Open Sans",Arial,sans-serif;color:var(--text)}
.abs{position:absolute}
.hero{left:0;top:0;width:1200px;height:675px}
.brand{left:69px;top:128px;display:flex;align-items:center;gap:10px;font-weight:700;font-size:30px;color:var(--blue)}
.brand-mark{width:22px;height:22px;background:var(--blue)}
.hero-title{left:69px;top:207px;font-size:42px;line-height:48px;font-weight:700;color:var(--red)}
.hero-sub{left:344px;top:542px;font-size:29px;line-height:42px;font-weight:700;color:var(--blue)}
.intro{left:342px;top:733px;width:520px;font-size:12.4px;line-height:20.6px;color:var(--text)}
.intro-cta{left:342px;top:856px;width:560px;font-size:25px;line-height:33px;font-weight:700;color:var(--red)}
.services-photo{left:0;top:1013px;width:723px;height:596px}
.service-list{left:350px;top:1016px;list-style:none;font-weight:700;font-size:37px;line-height:62px;color:var(--ink)}
.service-list .active{color:var(--red)}
.service-text{left:733px;top:1083px;width:380px;font-size:12.6px;line-height:20.6px;color:var(--text)}
.service-text p+p{margin-top:20.6px}
.gallery-title{left:95px;top:1722px;font-size:37px;font-weight:700;color:var(--red)}
.gallery{left:0;top:1812px;width:1200px;height:673px}
.footer{left:0;top:2648px;width:1200px;height:407px;background:var(--footer);color:var(--white)}
.footer-head{left:95px;top:52px;font-size:24px;font-weight:700}
.contact{left:95px;top:104px;font-size:33px;line-height:50px}
.legal{left:95px;top:226px;font-size:21px;line-height:32.5px}
.address{left:605px;top:104px;font-size:21px;line-height:32.5px}
.services-foot{left:605px;top:226px;font-size:21px;line-height:32.5px}
</style>
</head>
<body>

<header class="abs hero">
  <svg width="1200" height="675" viewBox="0 0 1200 675">
    <rect width="1200" height="675" fill="var(--hero-bg)"/>
    <polygon points="184,675 441,344 686,675" fill="var(--hero-shade)"/>
    <defs>
      <linearGradient id="lawnHero" x1="0" y1="0" x2="0" y2="1">
        <stop offset="0" stop-color="#c9d9ea"/>
        <stop offset="0.35" stop-color="#9aa7ab"/>
        <stop offset="0.5" stop-color="#7fb64a"/>
        <stop offset="1" stop-color="#3f8a22"/>
      </linearGradient>
    </defs>
    <polygon points="712,0 1200,0 1200,675 686,675 441,344" fill="url(#lawnHero)" role="img" aria-label="Foto: frisch gemähter Rasen vor einem Haus"/>
  </svg>
  <div class="abs brand"><span class="brand-mark"></span>Wohnpfleger</div>
  <h1 class="abs hero-title">GARTEN &amp;<br>LANDSCHAFTSBAU</h1>
  <p class="abs hero-sub">HAUSMEISTER<br>SERVICE</p>
</header>

<section>
  <p class="abs intro">Sie möchten das ihr Garten planvoll angelegt oder wirkungsvoll ergänzt wird?<br>Wir das Team von Wohnpfleger für Garten und Landschaftsbau, übernehmen das gerne für sie. Aufgrund unseres fundiertes Fachwissen und Jahre lange Erfahrung, verwandeln wir jeden Garten in ein persönliches und individuelles Traumreich. Im rahmen dessen führen wir auch Pflasterarbeiten sowie Zaunarbeiten aller Arten durch.</p>
  <h2 class="abs intro-cta">WIR FREUEN UNS AUF IHRE ANFRAGE UND IHREN AUFTRAG.</h2>
</section>

<section>
  <svg class="abs services-photo" viewBox="0 0 723 596">
    <defs>
      <linearGradient id="fenceTone" x1="0" y1="0" x2="1" y2="1">
        <stop offset="0" stop-color="#b57a45"/>
        <stop offset="0.7" stop-color="#9a6335"/>
        <stop offset="1" stop-color="#4f7d2c"/>
      </linearGradient>
    </defs>
    <polygon points="0,0 178,0 723,596 0,596" fill="url(#fenceTone)" role="img" aria-label="Foto: Holzzaun mit Rankgitter am Rasen"/>
  </svg>
  <ul class="abs service-list">
    <li>GARTENPFLEGE</li>
    <li class="active">ZAUNARBEITEN</li>
    <li>PFLASTERARBEITEN</li>
  </ul>
  <div class="abs service-text">
    <p>Mit unseren Zaunarbeiten bleibt alles auf der richtigen Seite der Grundstücksgrenze. Kinder und Haustiere drinnen, ungebetene Gäste draußen. Damit ihr neuer Zaun auch Optisch neu glänzt, bieten wir als Wohnpfleger unser ganzes können auf - und errichten ihren neuen Zaun ganz nach ihren Wünschen und Vorstellungen.</p>
    <p>Verlassen sie sich auf unsere Jahrelange Erfahrung in der Gartengestaltung. Wir errichten für sie Holz, Metallzäune und CO. Genau nach ihren Wünschen, zuverlässig und rechtzeitig zum vereinbarten Termin</p>
  </div>
</section>

<section>
  <h2 class="abs gallery-title">EINBLICK IN UNSERE ARBEITEN</h2>
  <svg class="abs gallery" viewBox="0 0 1012 567" preserveAspectRatio="none" role="img" aria-label="Fotocollage: Rasenflächen, Pflasterwege, Steinplatten und Gabionenzaun">
    <defs>
      <linearGradient id="lawnA" x1="0" y1="0" x2="0" y2="1">
        <stop offset="0" stop-color="#6d7d5e"/>
        <stop offset="0.35" stop-color="#7aa04c"/>
        <stop offset="1" stop-color="#5c9a35"/>
      </linearGradient>
      <linearGradient id="slate" x1="0" y1="0" x2="1" y2="1">
        <stop offset="0" stop-color="#7e8384"/>
        <stop offset="1" stop-color="#565b5d"/>
      </linearGradient>
      <linearGradient id="yard" x1="0" y1="0" x2="0" y2="1">
        <stop offset="0" stop-color="#d9dfe3"/>
        <stop offset="0.4" stop-color="#7c8f66"/>
        <stop offset="1" stop-color="#b9a785"/>
      </linearGradient>
      <linearGradient id="tiles" x1="0" y1="0" x2="1" y2="1">
        <stop offset="0" stop-color="#b4b8b8"/>
        <stop offset="1" stop-color="#7d8284"/>
      </linearGradient>
    </defs>
    <rect width="1012" height="567" fill="url(#lawnA)"/>
    <polygon points="475,162 600,0 830,0 595,300" fill="url(#yard)"/>
    <polygon points="372,296 475,162 595,300 770,567 580,567" fill="url(#slate)"/>
    <polygon points="155,567 372,296 580,567" fill="#4d5153"/>
    <polygon points="595,300 830,0 1012,0 1012,80 685,440" fill="url(#yard)"/>
    <polygon points="685,440 850,230 1012,430 1012,567 770,567" fill="url(#tiles)"/>
    <polygon points="850,230 950,100 1012,160 1012,430" fill="#7fa552"/>
    <polygon points="950,100 1012,20 1012,160" fill="#ffffff"/>
  </svg>
</section>

<footer class="abs footer">
  <h2 class="abs footer-head">WIR FREUEN UNS VON IHNEN ZU HÖREN</h2>
  <p class="abs contact">0176 - 512 409 27<br>kontakt@wohnpfleger.info</p>
  <p class="abs legal">©2023 Jonas Brandt<br>Impressum<br>Datenschutzerklärung</p>
  <p class="abs address">Jonas Brandt<br>Lindenweg 14<br>Musterstadt 12345</p>
  <p class="abs services-foot">Garten &amp; Landschaftsbau<br>Hausmeister Service</p>
</footer>

</body>
</html>
```